Global recruitment firm needs a design for marketing material

We need a design for our company Harlow Crest, which is a global recruitment firm specializing in senior finance and executive positions. This will be a template/ background for all our marketing material. We are looking to communicate a consistent message to current and existing clients. Uploaded below are our files describing our mission, values and strategy and story. Please also look at our website www.harlowcrest-demo.com.au. Examples of where this design will be used will be in client proposals, marketing info telling our story, social media content, infographics, and general client communication.

Target Market(s)

Client companies in the finance industry, Executive level finance candidates(CEO, CFO)

Requirements
Must have
• company logo, mission, value, strategy, website, our story
• Will be using the graphic for website, all communication with clients > looking for something to use for different purposes

```html
<!DOCTYPE html>
<html lang="en">
<head>
<meta charset="utf-8">
<title>Harlow Crest – Connecting Talent With Opportunity Globally</title>
<link rel="stylesheet" href="https://fonts.googleapis.com/css2?family=Mulish:wght@400;600;700&family=Oswald:wght@500&display=swap">
<style>
  :root {
    --white: #ffffff;
    --ink: #3a3a3a;
    --muted: #6d6d6d;
    --night-top: #0d1524;
    --night-bottom: #3a2a1c;
    --brand-blue: #1f7cc6;
    --yellow: #f7b83a;
    --yellow-band: #fdc43f;
    --green: #2fbf98;
    --blue: #3f7fdc;
    --value-blue: #4f8ff0;
    --card-grey: #ececec;
    --card-shadow: #d2d2d2;
    --footer: #353535;
    --footer-label: #4aa3f0;
    --footer-text: #e6e6e6;
    --rule: #8a8a8a;
  }
  * { margin: 0; padding: 0; box-sizing: border-box; }
  html, body { width: 1200px; height: 3416px; overflow: hidden; }
  body {
    position: relative;
    background: var(--white);
    font-family: "Mulish", "Century Gothic", sans-serif;
    color: var(--ink);
  }
  .abs { position: absolute; }

  /* Header */
  .hero-photo {
    left: 0; top: 0; width: 1200px; height: 695px;
    background: linear-gradient(180deg, var(--night-top) 0%, #1c2538 45%, #4a3a26 62%, #15171d 78%, var(--night-bottom) 100%);
  }
  .brand-name {
    left: 70px; top: 90px;
    font-size: 40px; font-weight: 700; color: var(--white);
    letter-spacing: 2px;
  }
  .call-us {
    right: 78px; top: 66px;
    font-size: 37px; font-weight: 700; color: var(--white);
    display: flex; align-items: center; gap: 12px;
  }
  .call-us svg { width: 34px; height: 34px; }

  /* Title */
  .title-box {
    left: 84px; top: 622px; width: 1039px; height: 289px;
    background: var(--brand-blue);
    display: flex; align-items: center; justify-content: center;
    text-align: center; color: var(--white);
    font-size: 55px; font-weight: 700; line-height: 70px;
  }

  /* Section headings */
  .section-title { font-size: 37px; font-weight: 700; color: var(--ink); }
  .strategy-title { left: 0; width: 1200px; top: 980px; text-align: center; }
  .strategy-title .dash { font-weight: 400; margin: 0 18px; }

  /* Strategy cards */
  .card { top: 1095px; width: 280px; height: 314px; }
  .card svg.shape { position: absolute; left: 0; top: 0; width: 284px; height: 318px; }
  .card-label {
    position: absolute; left: 38px; top: 40px;
    font-family: "Oswald", "Arial Narrow", sans-serif;
    font-weight: 500; font-size: 38px; line-height: 48px; color: var(--white);
  }
  .card-icon { position: absolute; right: 26px; bottom: 30px; width: 110px; height: 110px; }
  .card-engage { left: 134px; }
  .card-challenge { left: 463px; }
  .card-select { left: 792px; }

  /* Story */
  .story-band { left: 84px; top: 1489px; width: 1039px; height: 431px; background: var(--yellow-band); }
  .story-photo {
    left: 137px; top: 1548px; width: 307px; height: 308px;
    border-radius: 46% 54% 40% 60% / 52% 44% 56% 48%;
    background: linear-gradient(135deg, #d9d6d0 0%, #b99a7a 45%, #6f6a66 100%);
  }
  .story-text { left: 503px; top: 1540px; width: 545px; color: var(--white); }
  .story-text h2 { font-size: 37px; font-weight: 700; margin-bottom: 22px; }
  .body-copy { font-size: 27px; line-height: 42px; }

  /* Mission */
  .mission-text { left: 137px; top: 1972px; width: 570px; }
  .mission-text h2 { font-size: 37px; font-weight: 700; margin-bottom: 22px; }
  .mission-text p { color: var(--muted); }
  .mission-photo {
    left: 756px; top: 1977px; width: 310px; height: 318px;
    border-radius: 58% 42% 50% 50% / 40% 60% 40% 60%;
    background: linear-gradient(135deg, #8a9aa6 0%, #c9a27e 50%, #5a6f80 100%);
  }

  /* Value */
  .value-band { left: 84px; top: 2352px; width: 1039px; height: 540px; background: var(--value-blue); }
  .value-text { left: 84px; width: 1039px; top: 2400px; text-align: center; color: var(--white); }
  .value-text h2 { font-size: 37px; font-weight: 700; margin-bottom: 22px; }
  .value-text p { width: 900px; margin: 0 auto; }
  .devices {
    left: 200px; top: 2641px; width: 768px; height: 360px;
    background: linear-gradient(180deg, #20283a 0%, #3b3f4a 70%, #c9ccd2 100%);
    border-radius: 12px;
  }

  /* Footer */
  .footer { left: 0; top: 3088px; width: 1200px; height: 328px; background: var(--footer); color: var(--footer-text); }
  .footer-contacts {
    position: absolute; left: 0; width: 1200px; top: 68px;
    text-align: center; font-size: 28px;
  }
  .footer-contacts .label { color: var(--footer-label); font-weight: 700; }
  .footer-contacts .gap { display: inline-block; width: 42px; }
  .footer-social { position: absolute; left: 140px; top: 138px; width: 920px; height: 48px; }
  .footer-social .rule { position: absolute; top: 23px; height: 2px; width: 350px; background: var(--rule); }
  .footer-social .rule.left { left: 0; }
  .footer-social .rule.right { right: 0; }
  .footer-social .dots { position: absolute; left: 380px; width: 160px; display: flex; justify-content: space-between; }
  .footer-social .dot { width: 46px; height: 46px; border-radius: 50%; background: #7a7a7a; }
  .footer-social .dot.mid { background: #2f8fd8; }
  .footer-legal {
    position: absolute; left: 0; width: 1200px; top: 222px;
    text-align: center; font-size: 28px;
  }
  .footer-legal .sep { margin: 0 36px; }
</style>
</head>
<body>

  <div class="abs hero-photo" role="img" aria-label="Night photograph of an illuminated arch bridge reflected in a river"></div>
  <div class="abs brand-name">Harlow Crest</div>
  <div class="abs call-us">
    Call Us:
    <svg viewBox="0 0 24 24" aria-hidden="true"><path fill="#ffffff" d="M6.6 10.8a15.2 15.2 0 0 0 6.6 6.6l2.2-2.2c.3-.3.7-.4 1-.2 1.1.4 2.3.6 3.6.6.6 0 1 .4 1 1V20c0 .6-.4 1-1 1A17 17 0 0 1 3 4c0-.6.4-1 1-1h3.5c.6 0 1 .4 1 1 0 1.3.2 2.5.6 3.6.1.3 0 .7-.2 1z"/></svg>
    +61 400-555-017
  </div>

  <div class="abs title-box">Connecting Talent<br>With Opportunity Globally</div>

  <div class="abs section-title strategy-title"><span class="dash">--</span>Our Strategy<span class="dash">--</span></div>

  <div class="abs card card-engage">
    <svg class="shape" viewBox="0 0 284 318" aria-hidden="true">
      <path d="M18 4 H194 Q284 4 284 94 V304 Q284 318 270 318 H18 Q4 318 4 304 V18 Q4 4 18 4 Z" fill="var(--card-shadow)"/>
      <path d="M14 0 H190 Q280 0 280 90 V300 Q280 314 266 314 H14 Q0 314 0 300 V14 Q0 0 14 0 Z" fill="var(--card-grey)"/>
      <path d="M14 0 H238 C232 150 150 250 0 292 V14 Q0 0 14 0 Z" fill="var(--yellow)"/>
    </svg>
    <div class="card-label">01<br>Engage</div>
    <svg class="card-icon" viewBox="0 0 110 110" role="img" aria-label="Handshake icon">
      <g fill="var(--yellow)">
        <rect x="4" y="70" width="22" height="34" rx="3" transform="rotate(-45 15 87)"/>
        <rect x="84" y="6" width="22" height="34" rx="3" transform="rotate(-45 95 23)"/>
        <path d="M22 72 L56 38 Q64 30 74 34 L84 40 L52 84 Q44 92 36 86 Z"/>
        <path d="M40 56 L70 30 Q78 24 86 32 L72 52 Z" fill="#e9a42a"/>
      </g>
      <g fill="var(--card-grey)">
        <rect x="48" y="58" width="5" height="16" rx="2" transform="rotate(45 50 66)"/>
        <rect x="57" y="50" width="5" height="16" rx="2" transform="rotate(45 59 58)"/>
        <rect x="66" y="42" width="5" height="14" rx="2" transform="rotate(45 68 49)"/>
      </g>
    </svg>
  </div>

  <div class="abs card card-challenge">
    <svg class="shape" viewBox="0 0 284 318" aria-hidden="true">
      <path d="M18 4 H194 Q284 4 284 94 V304 Q284 318 270 318 H18 Q4 318 4 304 V18 Q4 4 18 4 Z" fill="var(--card-shadow)"/>
      <path d="M14 0 H190 Q280 0 280 90 V300 Q280 314 266 314 H14 Q0 314 0 300 V14 Q0 0 14 0 Z" fill="var(--card-grey)"/>
      <path d="M14 0 H238 C232 150 150 250 0 292 V14 Q0 0 14 0 Z" fill="var(--green)"/>
    </svg>
    <div class="card-label">02<br>Challenge</div>
    <svg class="card-icon" viewBox="0 0 110 110" aria-hidden="true">
      <circle cx="52" cy="58" r="44" fill="var(--green)"/>
      <circle cx="52" cy="58" r="32" fill="var(--card-grey)"/>
      <circle cx="52" cy="58" r="20" fill="var(--green)"/>
      <circle cx="52" cy="58" r="9" fill="var(--card-grey)"/>
      <path d="M54 56 L92 18" stroke="var(--green)" stroke-width="6" stroke-linecap="round"/>
      <path d="M84 12 L100 10 L98 26 Z" fill="var(--green)"/>
    </svg>
  </div>

  <div class="abs card card-select">
    <svg class="shape" viewBox="0 0 284 318" aria-hidden="true">
      <path d="M18 4 H194 Q284 4 284 94 V304 Q284 318 270 318 H18 Q4 318 4 304 V18 Q4 4 18 4 Z" fill="var(--card-shadow)"/>
      <path d="M14 0 H190 Q280 0 280 90 V300 Q280 314 266 314 H14 Q0 314 0 300 V14 Q0 0 14 0 Z" fill="var(--card-grey)"/>
      <path d="M14 0 H238 C232 150 150 250 0 292 V14 Q0 0 14 0 Z" fill="var(--blue)"/>
    </svg>
    <div class="card-label">03<br>Select</div>
    <svg class="card-icon" viewBox="0 0 110 110" aria-hidden="true">
      <path d="M44 40 L96 64 L72 70 L88 96 L78 102 L62 76 L46 92 Z" fill="var(--blue)"/>
      <g stroke="var(--blue)" stroke-width="4" stroke-linecap="round">
        <path d="M40 14 V28"/><path d="M14 38 H28"/><path d="M20 18 L29 27"/><path d="M60 20 L53 29"/><path d="M18 60 L27 52"/>
      </g>
    </svg>
  </div>

  <div class="abs story-band"></div>
  <div class="abs story-photo" role="img" aria-label="Photograph of two business people shaking hands in an office"></div>
  <div class="abs story-text">
    <h2>Our Story ----</h2>
    <p class="body-copy">30 years of experience enables us to partner with our clients to challenge the recruitment strategy on people, positions and the process, to build high perform-ing finance teams ...</p>
  </div>

  <div class="abs mission-text">
    <h2>Our Mission ----</h2>
    <p class="body-copy">Harlow Crest is a global search firm originating in Sydney in 2010 and today partnering with finance professionals in Australia, Hong Kong, Singapore, India, London, United States and Canada ...</p>
  </div>
  <div class="abs mission-photo" role="img" aria-label="Photograph of hands joining coloured puzzle pieces"></div>

  <div class="abs value-band"></div>
  <div class="abs value-text">
    <h2>-- Our Value --</h2>
    <p class="body-copy">There are many variations of passages of lorem site that<br>Lorem Ipsum available, but the majority have suffered alteration in<br>form, by injected humour then proud to be ...</p>
  </div>
  <div class="abs devices" role="img" aria-label="Mockup of the website shown on a desktop monitor, a laptop and a tablet"></div>

  <footer class="abs footer">
    <div class="footer-contacts">
      <span class="label">Phone:</span> +61 400-555-017<span class="gap"></span><span class="label">Email:</span> hello@harlowcrest-demo.com.au
    </div>
    <div class="footer-social" aria-hidden="true">
      <span class="rule left"></span>
      <div class="dots"><span class="dot"></span><span class="dot mid"></span><span class="dot"></span></div>
      <span class="rule right"></span>
    </div>
    <div class="footer-legal">© 2018 Harlow Crest.<span class="sep">|</span>www.harlowcrest-demo.com.au</div>
  </footer>

</body>
</html>
```